Crumbs Crumbs - Home baking business needs a business card design. I sell at artisan food festivals.

A design for rebranding my baking business which serves artisan food festivals in the UK. Produce is locally sourced, homegrown or foraged, I make rustic unusual recipes. I would like a simple design using classic colours. I like green, 'Wrenby and Holt". I like chunky lettering, but very open to new ideas/designs. On the reverse side I would like a singular symbol demonstrating baking either a bowl and wooden spoon or cake and the facebook icon with CrumbsCrumbs

Reason: I would like to progress with the design by Tessa Marlow 4827305 . I misunderstood the deadline itinerary but would very much like to go ahead with your design. thanks

Target Market(s)

customers at food festivals, other small food businesses

Industry/Entity Type

Business

Contact Information for Business Card

Minimal amount of type on the card. Design to accentuate the look of my stall and style of baking . I display cakes on either old slate tiles, old palette boxes. Prices are hand written on brown luggage labels

Font styles to use
Other font styles liked:
• Blair MdiTC

Requirements
Must have
• Underneath Crumbs Crumbs i would like to have homemade by Pam somewhere on the front of the card.
Nice to have
• Clear lettering, classic colours i.e. Wrenby and Holt colour palettes.
Should not have
• Fancy, blingy, wordy,

```html
<!DOCTYPE html>
<html lang="en">
<head>
<meta charset="utf-8">
<title>Crumbs Crumbs – Business Card</title>
<link href="https://fonts.googleapis.com/css2?family=Montserrat:wght@300;400;500&display=swap" rel="stylesheet">
<style>
  :root {
    --page-bg: #eeeeec;
    --card-bg: #fbfbfa;
    --dot-ink: #2b2b2b;
    --gold: #c39a4e;
    --ink: #1f1f1f;
  }
  * { box-sizing: border-box; margin: 0; padding: 0; }
  html, body {
    width: 1200px;
    height: 800px;
    overflow: hidden;
    background: var(--page-bg);
    font-family: "Montserrat", Arial, sans-serif;
  }
  .canvas {
    width: 1200px;
    height: 800px;
    display: flex;
    flex-direction: column;
    align-items: center;
    justify-content: center;
    gap: 50px;
  }
  .card {
    position: relative;
    width: 600px;
    height: 340px;
    background: var(--card-bg);
    box-shadow: 0 2px 10px rgba(0,0,0,0.08);
  }
  .card__dots {
    position: absolute;
    inset: 0;
    width: 100%;
    height: 100%;
  }
  .brand {
    position: relative;
    text-align: center;
    color: var(--gold);
    white-space: nowrap;
  }
  .brand__name {
    font-weight: 400;
    letter-spacing: 0.02em;
    line-height: 1;
  }
  .brand__tagline {
    font-weight: 400;
    text-transform: uppercase;
    letter-spacing: 0.3em;
    margin-top: 12px;
  }
  .card--front {
    display: flex;
    align-items: center;
    justify-content: center;
  }
  .card--front .brand__name { font-size: 50px; }
  .card--front .brand__tagline { font-size: 15px; }

  .card--back {
    display: flex;
    align-items: center;
    padding: 0 44px 0 48px;
    gap: 34px;
  }
  .card--back .brand { flex: none; width: 214px; }
  .card--back .brand__name { font-size: 27px; }
  .card--back .brand__tagline { font-size: 9px; margin-top: 8px; letter-spacing: 0.24em; }

  .contact { color: var(--ink); white-space: nowrap; }
  .contact__name {
    font-size: 29px;
    font-weight: 400;
    letter-spacing: 0.01em;
    margin-bottom: 8px;
  }
  .contact__line {
    display: flex;
    align-items: center;
    gap: 10px;
    font-size: 18px;
    font-weight: 300;
    line-height: 1.4;
  }
  .contact__icon { width: 13px; height: 13px; flex: none; }
</style>
</head>
<body>
<main class="canvas">

  <section class="card card--front" aria-label="Card front">
    <svg class="card__dots" viewBox="0 0 600 340" aria-hidden="true">
      <rect x="22" y="22" width="556" height="296" fill="none" stroke="var(--dot-ink)" stroke-width="13" stroke-linecap="round" stroke-dasharray="0 37.07" opacity="0.9"/>
    </svg>
    <div class="brand">
      <p class="brand__name">Crumbs Crumbs</p>
      <p class="brand__tagline">Homemade by Pam</p>
    </div>
  </section>

  <section class="card card--back" aria-label="Card back">
    <svg class="card__dots" viewBox="0 0 600 340" aria-hidden="true">
      <rect x="22" y="22" width="556" height="296" fill="none" stroke="var(--dot-ink)" stroke-width="13" stroke-linecap="round" stroke-dasharray="0 37.07" opacity="0.9"/>
    </svg>
    <div class="brand">
      <p class="brand__name">Crumbs Crumbs</p>
      <p class="brand__tagline">Homemade by Pam</p>
    </div>
    <div class="contact">
      <p class="contact__name">PAM SURNAME</p>
      <p class="contact__line">
        <svg class="contact__icon" viewBox="0 0 24 24" aria-hidden="true"><path fill="var(--ink)" d="M6.6 10.8a15.1 15.1 0 0 0 6.6 6.6l2.2-2.2a1 1 0 0 1 1-.25 11.4 11.4 0 0 0 3.6.57 1 1 0 0 1 1 1V20a1 1 0 0 1-1 1A17 17 0 0 1 3 4a1 1 0 0 1 1-1h3.5a1 1 0 0 1 1 1c0 1.250.2 2.45.57 3.57a1 1 0 0 1-.25 1z"/></svg>
        01632 960 418
      </p>
      <p class="contact__line">
        <svg class="contact__icon" viewBox="0 0 24 24" aria-hidden="true"><circle cx="12" cy="12" r="10" fill="var(--ink)"/></svg>
        CrumbsCrumbs
      </p>
    </div>
  </section>

</main>
</body>
</html>
```